依頼詳細
●デザインの要望
・少し温かみ、やわらかさのあるデザイン(まるっこすぎない)
※参考例:poruくらいのやわらかさ
・そのほかの色については特に指定なし(現在の青は入れなくてOKです)
⇒カラフルにするかどうかもデザインの中で考えて頂いて結構です
・現在のアプリにある下記のボタンを全て実装する
※投稿ボタン、画面更新ボタン、履歴ボタン、オプションボタン、カテゴリ選択ボタン の5個
・投稿が表示されるマス目は正方形だけでなく長方形等もまぜてほしい
※現在は正方形オンリーですが、縦に2個くっつけたものや横に2個くっつけたものが入ってきたりするデザイン
⇒アプリ:Tiledeck の記事一覧画面のようなイメージ
・zelvonなのでzvos7のフラットなイメージ(がっつり立体的にはしてほしくないです)

●納品物
PSDファイル1個(zelvonで使用する倍のサイズの 1920x1280 くらいで作ってください)
可能であればレイヤーのあるPNGファイル(可能であればで結構です)

サイトURL
https://apps.trovenlo.jp/jp/app/id518203764?mt=8
ページ数
1ページ
希望イメージ
シンプル 複雑
単色 カラフル
暗い 明るい
日常 高級
遊び心 厳粛
未来的 伝統的
女性的 男性的
希望する色
小豆色や薄い茶色等温かみのある色全般
納品ファイル
• フォトショップ形式 (.psd)
• PNG形式 (.png)
補足説明
■ 選んだ理由

やわらかいテイストでかつ既存の青をさし色に入れて頂けたこと、
またプラスアルファとしてスプラッシュスクリーンをご提示いただけたため、
より実装後のアプリのイメージがわくことができました。

■ 提案者全員のお礼・コメント

たくさんのご提案ありがとうございました。
特にUIそのものまで提案して頂けたりと非常にこちらとしても勉強になる案件となりました。

上部のバーのデザインや、吹き出し型のデザイン、カラフル、マット等
かなり悩ませていただきました。
最終的にはより女性的で、かつ落ち着いている
という部分を基準に選ぶことにしました。

本アプリは今後もどんどん改良を加える予定のため、
また機会が有りましたら是非宜しくお願い致します。

```html
<!DOCTYPE html>
<html lang="ja">
<head>
<meta charset="utf-8">
<title>全体 — タイル一覧</title>
<link rel="stylesheet" href="https://fonts.googleapis.com/css2?family=Noto+Sans+JP:wght@400;500;700&display=swap">
<style>
  :root{
    --bar:#352b24;
    --bar-text:#f3ece2;
    --ground:#ebe4d7;
    --tile-brown:#7b6a5b;
    --tile-dark:#5a4a3d;
    --tile-red:#c75a31;
    --tile-green:#7d9b6c;
    --tile-blue:#7d9cae;
    --tile-orange:#df9f3e;
    --tile-text:#fbf6ee;
    --ad-top:#cfcfcf;
    --ad-bottom:#9a9a9a;
  }
  *{margin:0;padding:0;box-sizing:border-box}
  html,body{width:800px;height:1200px;overflow:hidden;background:var(--ground)}
  body{font-family:"Noto Sans JP",sans-serif;position:relative}
  .status-bar{position:absolute;left:0;top:0;width:800px;height:53px;background:var(--bar);color:var(--bar-text);font-size:26px;display:flex;align-items:center;padding:0 14px}
  .status-bar .carrier{flex:1}
  .status-bar .clock{position:absolute;left:0;right:0;text-align:center;font-weight:500}
  .status-bar .battery{display:flex;align-items:center;gap:8px}
  .nav-bar{position:absolute;left:0;top:53px;width:800px;height:112px;background:var(--bar);color:var(--bar-text)}
  .nav-bar .options-button{position:absolute;left:34px;top:38px}
  .nav-bar .post-button{position:absolute;right:34px;top:36px}
  .nav-bar .category-title{position:absolute;left:0;right:0;top:32px;text-align:center;font-size:36px;font-weight:700;letter-spacing:2px}
  .nav-bar .refresh-button{vertical-align:-4px;margin-left:6px}
  .tile-grid{position:absolute;left:0;top:165px;width:800px;height:902px;overflow:hidden;background:var(--ground)}
  .tile{position:absolute;overflow:hidden;color:var(--tile-text);font-size:24px;line-height:1.55;font-weight:500}
  .tile p{position:absolute;white-space:nowrap}
  .brown{background:var(--tile-brown)}
  .dark{background:var(--tile-dark)}
  .red{background:var(--tile-red)}
  .green{background:var(--tile-green)}
  .blue{background:var(--tile-blue)}
  .orange{background:var(--tile-orange)}
  .history-button{position:absolute;left:0;top:973px;width:98px;height:94px;background:var(--ground);display:flex;align-items:center;justify-content:center}
  .ad-banner{position:absolute;left:0;top:1067px;width:800px;height:133px;background:linear-gradient(var(--ad-top),var(--ad-bottom))}
</style>
</head>
<body>
  <header class="status-bar">
    <span class="carrier">●●●●○ SoraTel</span>
    <span class="clock">23:22</span>
    <span class="battery">63%
      <svg width="46" height="22" viewBox="0 0 46 22"><rect x="1" y="1" width="40" height="20" rx="3" fill="none" stroke="#f3ece2" stroke-width="2"/><rect x="4" y="4" width="23" height="14" fill="#f3ece2"/><rect x="42" y="7" width="3" height="8" fill="#f3ece2"/></svg>
    </span>
  </header>

  <nav class="nav-bar">
    <svg class="options-button" width="40" height="40" viewBox="0 0 40 40" aria-label="オプション">
      <g fill="none" stroke="#f3ece2" stroke-width="4">
        <circle cx="20" cy="20" r="11"/>
        <circle cx="20" cy="20" r="4"/>
        <path d="M20 2v7M20 31v7M2 20h7M31 20h7M7 7l5 5M28 28l5 5M7 33l5-5M28 12l5-5"/>
      </g>
    </svg>
    <div class="category-title">全体<svg class="refresh-button" width="30" height="30" viewBox="0 0 30 30" aria-label="更新"><path d="M24 15a9 9 0 1 1-3-6.7" fill="none" stroke="#f3ece2" stroke-width="3.5"/><path d="M17 4h7v7" fill="none" stroke="#f3ece2" stroke-width="3.5"/></svg></div>
    <svg class="post-button" width="44" height="44" viewBox="0 0 44 44" aria-label="投稿">
      <g fill="none" stroke="#f3ece2" stroke-width="3.5">
        <path d="M22 4H4v36h36V22"/>
        <path d="M38 4l4 4-20 20h-4v-4z"/>
      </g>
    </svg>
  </nav>

  <main class="tile-grid">
    <!-- top partial row -->
    <div class="tile orange" style="left:12px;top:7px;width:113px;height:53px"></div>
    <div class="tile brown"  style="left:136px;top:7px;width:259px;height:53px"></div>
    <div class="tile brown"  style="left:405px;top:7px;width:250px;height:53px"></div>
    <div class="tile red"    style="left:665px;top:7px;width:140px;height:53px"></div>

    <div class="tile brown" style="left:0;top:68px;width:125px;height:519px">
      <p style="right:6px;top:34px">なに言の</p>
      <p style="right:6px;top:190px">いつも<br>いてる<br>いのっ</p>
      <p style="right:6px;top:330px">つたわ<br>わんね</p>
    </div>
    <div class="tile red" style="left:136px;top:68px;width:259px;height:327px">
      <p style="left:46px;top:38px">やっぱり好き</p>
      <p style="left:46px;top:100px">大好き</p>
    </div>
    <div class="tile green" style="left:136px;top:405px;width:259px;height:182px">
      <p style="left:30px;top:40px">ここって本音書<br>けるから<br>ほんと楽。</p>
    </div>
    <div class="tile brown" style="left:405px;top:68px;width:250px;height:327px">
      <p style="left:30px;top:60px">いっそ会社やめ<br>ちゃうか〜。</p>
    </div>
    <div class="tile dark" style="left:405px;top:405px;width:250px;height:182px">
      <p style="left:30px;top:40px">まじなんなの？<br>俺だけが悪者か<br>よ。</p>
    </div>
    <div class="tile brown" style="left:665px;top:68px;width:140px;height:257px">
      <p style="left:24px;top:22px">みんな<br>いなく<br>いん、ど<br>な。</p>
    </div>
    <div class="tile blue" style="left:665px;top:333px;width:140px;height:254px">
      <p style="left:24px;top:50px">Chirpline<br>ことが</p>
    </div>

    <div class="tile blue" style="left:0;top:595px;width:125px;height:267px">
      <p style="right:6px;top:26px">たしが<br>せない<br>う為</p>
    </div>
    <div class="tile red" style="left:136px;top:595px;width:259px;height:267px">
      <p style="left:28px;top:44px">一回でもいいから<br>また会いたい<br>時間もどれ…</p>
    </div>
    <div class="tile brown" style="left:405px;top:595px;width:400px;height:267px">
      <p style="left:30px;top:44px">死んでほしい<br>生きないで<br>なんで私が我慢しなきゃいけない<br>の？<br>陰口聴こえないとか思ってんの</p>
    </div>

    <!-- bottom partial row -->
    <div class="tile brown"  style="left:0;top:870px;width:125px;height:40px"></div>
    <div class="tile brown"  style="left:136px;top:870px;width:259px;height:40px"></div>
    <div class="tile orange" style="left:405px;top:870px;width:250px;height:40px"></div>
    <div class="tile brown"  style="left:665px;top:870px;width:140px;height:40px"></div>
  </main>

  <div class="history-button" aria-label="履歴">
    <svg width="44" height="40" viewBox="0 0 44 40"><path d="M22 4C11 4 4 10.5 4 18c0 4 2 7.5 5.5 10L7 36l9-4.5c2 .5 4 .8 6 .8 11 0 18-6.5 18-14.3S33 4 22 4z" fill="none" stroke="#352b24" stroke-width="3.5"/></svg>
  </div>

  <aside class="ad-banner" role="img" aria-label="ゲーム広告バナー（キャラクターイラストと石垣の背景）"></aside>
</body>
</html>
```